Real estate agent : RT Estates

I have done the attached logo designed by your company .
My business card description as below:
Name : Daniel Brooks
Mobile: 0412583047
Email : danielb@rtestates-demo.net.au
Sales & Property Management

```html
<!DOCTYPE html>
<html lang="en">
<head>
<meta charset="utf-8">
<title>RT Estates – Business Card</title>
<link href="https://fonts.googleapis.com/css2?family=Arimo:wght@400;700&display=swap" rel="stylesheet">
<style>
  :root {
    --ink: #161719;
    --paper: #ffffff;
    --rule: #e3e3e3;
    --text: #111111;
    --label: #222222;
  }
  * { margin: 0; padding: 0; box-sizing: border-box; }
  html, body {
    width: 1200px; height: 366px; overflow: hidden;
    background: var(--paper);
    font-family: "Arimo", Arial, sans-serif;
    color: var(--text);
  }
  .sheet { position: relative; width: 1200px; height: 366px; }
  .side-label {
    position: absolute; font-size: 19px; color: var(--label);
    transform: translateX(-50%);
  }
  .side-label--front { left: 285px; top: -4px; }
  .side-label--back { left: 921px; top: 3px; }

  .card { position: absolute; top: 44px; height: 321px; }
  .card--front {
    left: 0; width: 571px; display: flex;
    border: 1px solid var(--rule); background: var(--paper);
  }
  .card--back { left: 628px; width: 570px; background: var(--ink); }

  .brand-panel {
    width: 270px; height: 100%; background: var(--ink);
    display: flex; align-items: center; justify-content: center;
  }
  .brand {
    display: flex; align-items: center; gap: 10px;
    color: var(--paper); font-weight: 700; letter-spacing: 0.5px;
  }
  .brand__mark { background: var(--paper); }
  .brand--small { font-size: 24px; }
  .brand--small .brand__mark { width: 14px; height: 14px; }
  .brand--large { font-size: 38px; }
  .brand--large .brand__mark { width: 22px; height: 22px; }

  .details { position: relative; flex: 1; }
  .details__name {
    position: absolute; left: 27px; top: 64px;
    font-size: 19px; font-weight: 700;
  }
  .details__role {
    position: absolute; left: 27px; top: 91px;
    font-size: 13.5px; line-height: 20.5px;
  }
  .contact {
    position: absolute; left: 23px; display: flex; align-items: center;
    font-size: 16px;
  }
  .contact svg { width: 18px; height: 18px; margin-right: 12px; }
  .contact--phone { top: 197px; }
  .contact--email { top: 224px; font-size: 15px; }

  .card--back { display: flex; align-items: center; justify-content: center; }
</style>
</head>
<body>
<div class="sheet">
  <span class="side-label side-label--front">front</span>
  <span class="side-label side-label--back">Back</span>

  <section class="card card--front">
    <div class="brand-panel">
      <div class="brand brand--small"><span class="brand__mark"></span>RT Estates</div>
    </div>
    <div class="details">
      <h1 class="details__name">Daniel Brooks</h1>
      <p class="details__role">Managing Director<br>Sales &amp; Property Management</p>
      <p class="contact contact--phone">
        <svg viewBox="0 0 18 18" aria-hidden="true">
          <rect x="4" y="1" width="10" height="16" rx="2" fill="none" stroke="#111" stroke-width="2"/>
          <rect x="6" y="12.5" width="6" height="2" fill="#111"/>
        </svg>
        0412583047
      </p>
      <p class="contact contact--email">
        <svg viewBox="0 0 18 18" aria-hidden="true">
          <rect x="1" y="4" width="16" height="11" fill="#111"/>
          <path d="M1.5 4.5 L9 10.5 L16.5 4.5 M1.5 14.5 L7 9.5 M16.5 14.5 L11 9.5" fill="none" stroke="#fff" stroke-width="1.2"/>
        </svg>
        danielb@rtestates-demo.net.au
      </p>
    </div>
  </section>

  <section class="card card--back">
    <div class="brand brand--large"><span class="brand__mark"></span>RT Estates</div>
  </section>
</div>
</body>
</html>
```